Duel Business card

Want an edgy business card that shows both of our companies on each side of the card, OR both together with a cool design.

*Must be edgy: We have attached our two business logos. We are a bail bond and immigration bond company.

Would like the address on one side only.
Need Phone, cell, website, address, and Name

Company Name 1: Cellgate Release Partners
www.cellgatereleasepartners.example

Company Name 2: Borderline Surety Associates
www.borderlinesuretyassociates.example

These cards will need to be easily changeable so I can modify new employees

Target Market(s)

people in jail, takign imigrants out of jail and from being taken back to there country

Industry/Entity Type

Business

Requirements
Must have
• Include both logos attached

```html
<!DOCTYPE html>
<html lang="en">
<head>
<meta charset="utf-8">
<title>Dual Business Card – Cellgate Release Partners &amp; Borderline Surety Associates</title>
<link rel="stylesheet" href="https://fonts.googleapis.com/css2?family=Open+Sans:wght@400;600;700;800&display=swap">
<style>
  :root {
    --bg: #e9e6e1;
    --card-blue: #2b4ea8;
    --card-blue-light: #3e63bf;
    --card-blue-dark: #203f93;
    --band-yellow: #efd12b;
    --band-red: #e63a2e;
    --ink-white: #ffffff;
    --ink-blue: #26479e;
    --faint: rgba(255, 255, 255, 0.12);
    --shadow: 0 12px 30px rgba(0, 0, 0, 0.25);
  }
  * { box-sizing: border-box; margin: 0; padding: 0; }
  html, body {
    width: 1200px; height: 900px; overflow: hidden;
    background: var(--bg);
    font-family: "Open Sans", Arial, sans-serif;
  }
  .canvas {
    width: 1200px; height: 900px;
    display: flex; flex-direction: column; align-items: center;
    justify-content: center; gap: 40px;
  }
  .card {
    width: 700px; height: 400px; position: relative; overflow: hidden;
    box-shadow: var(--shadow);
    background: radial-gradient(ellipse at 50% 40%, var(--card-blue-light), var(--card-blue) 55%, var(--card-blue-dark));
  }

  /* Back side: both company names */
  .card-back {
    display: flex; align-items: center; justify-content: space-around; padding: 0 40px;
  }
  .brand {
    display: flex; align-items: center; gap: 14px; max-width: 290px;
  }
  .brand-dot {
    flex: none; width: 58px; height: 58px; border-radius: 50%;
  }
  .brand-dot--yellow { background: var(--band-yellow); }
  .brand-dot--red { background: var(--band-red); }
  .brand-name {
    color: var(--ink-white); font-weight: 800; font-size: 27px; line-height: 1.1;
    text-transform: uppercase;
  }

  /* Front side: contact details */
  .band {
    position: absolute; left: 0; right: 0;
    display: flex; align-items: center; justify-content: center;
    font-weight: 700; letter-spacing: 0.3px;
  }
  .band-top {
    top: 0; height: 68px; background: var(--band-yellow); color: var(--ink-blue); font-size: 20px;
  }
  .band-bottom {
    bottom: 0; height: 78px; background: var(--band-red); color: var(--ink-white); font-size: 21px;
  }
  .faint-mark {
    position: absolute; top: 110px; width: 190px; height: 190px; border-radius: 50%;
    background: var(--faint);
  }
  .faint-mark--left { left: -30px; }
  .faint-mark--right { right: -30px; }
  .contact {
    position: absolute; top: 68px; bottom: 78px; left: 0; right: 0;
    display: flex; flex-direction: column; align-items: center; justify-content: center;
    color: var(--ink-white); text-align: center;
  }
  .contact-name { font-size: 34px; font-weight: 700; margin-bottom: 8px; }
  .contact-label {
    font-size: 10px; font-weight: 700; letter-spacing: 0.5px; text-transform: uppercase;
    margin-top: 6px; line-height: 1;
  }
  .contact-value { font-size: 20px; font-weight: 400; line-height: 1.15; }
</style>
</head>
<body>
<main class="canvas">

  <section class="card card-back" aria-label="Card back">
    <div class="brand">
      <span class="brand-dot brand-dot--yellow"></span>
      <span class="brand-name">Cellgate Release Partners</span>
    </div>
    <div class="brand">
      <span class="brand-dot brand-dot--red"></span>
      <span class="brand-name">Borderline Surety Associates</span>
    </div>
  </section>

  <section class="card card-front" aria-label="Card front">
    <div class="band band-top">www.cellgatereleasepartners.example</div>
    <span class="faint-mark faint-mark--left"></span>
    <span class="faint-mark faint-mark--right"></span>
    <div class="contact">
      <p class="contact-name">Dana Whitfield</p>
      <p class="contact-label">Mobile</p>
      <p class="contact-value">800-555-0147</p>
      <p class="contact-label">Phone</p>
      <p class="contact-value">800-555-0147</p>
      <p class="contact-label">Address</p>
      <p class="contact-value">415 N. Harbor Point Ave.<br>Silver Ridge, NV 89000</p>
    </div>
    <div class="band band-bottom">www.borderlinesuretyassociates.example</div>
  </section>

</main>
</body>
</html>
```